Need business cards for our e-assessment business

We need professional looking business cards for our e-assessment business based in Europe. Our company is called Velnor.

You can just use sample name and addresses.

The colours we use are:

#70abe4 (blue)
#FF6600 (orange)

The back side should say: Assessments made simple

This is the print-shop we are using. Please look at the link for info about formats: http://nl.printqet.com/help/faq/using-my-own-artwork.html

Target Market(s)

Target market is education and large corporations

Industry/Entity Type

Business

```html
<!DOCTYPE html>
<html lang="en">
<head>
<meta charset="utf-8">
<title>Velnor business cards</title>
<link rel="stylesheet" href="https://fonts.googleapis.com/css2?family=Barlow:wght@400;500&display=swap">
<style>
  :root {
    --brand-orange: #ff6600;
    --brand-blue: #70abe4;
    --ink: #3a3a3a;
    --card: #f7f7f6;
    --backdrop: #e6e7e9;
  }
  * { margin: 0; padding: 0; box-sizing: border-box; }
  html, body {
    width: 1200px;
    height: 800px;
    overflow: hidden;
  }
  body {
    position: relative;
    background: var(--backdrop);
    font-family: "Barlow", sans-serif;
    color: var(--ink);
  }
  .card {
    position: absolute;
    left: 377px;
    width: 476px;
    background: var(--card);
  }
  .card--front { top: 76px; height: 303px; }
  .card--back { top: 417px; height: 311px; }

  .front-disc {
    position: absolute;
    left: 159px;
    top: 55px;
    width: 152px;
    height: 152px;
    border-radius: 50%;
    background: var(--brand-orange);
  }
  .tagline-rule {
    position: absolute;
    left: 149px;
    top: 250px;
    width: 178px;
    height: 2px;
    background: var(--brand-blue);
  }
  .tagline {
    position: absolute;
    left: 0;
    right: 0;
    top: 256px;
    text-align: center;
    font-size: 15px;
    letter-spacing: 0.3px;
    color: var(--brand-blue);
  }

  .brand-disc {
    position: absolute;
    left: 41px;
    top: 24px;
    width: 78px;
    height: 78px;
    border-radius: 50%;
    background: var(--brand-orange);
  }
  .brand-name {
    position: absolute;
    left: 138px;
    top: 30px;
    font-size: 54px;
    font-weight: 500;
    line-height: 1;
    color: var(--ink);
  }
  .person {
    position: absolute;
    left: 40px;
    top: 143px;
  }
  .person-name {
    font-size: 21px;
    font-weight: 400;
    letter-spacing: 0.3px;
  }
  .person-role {
    margin-top: 2px;
    font-size: 14px;
    letter-spacing: 1px;
  }
  .contact {
    position: absolute;
    left: 268px;
    top: 151px;
    font-size: 13px;
    line-height: 17px;
    list-style: none;
    letter-spacing: 0.3px;
  }
  .contact-key {
    display: inline-block;
    width: 17px;
    color: var(--brand-blue);
  }
  .address {
    position: absolute;
    left: 268px;
    top: 234px;
    font-size: 13px;
    line-height: 17px;
    font-style: normal;
    letter-spacing: 0.3px;
  }
  .website {
    position: absolute;
    left: 40px;
    top: 266px;
    font-size: 13px;
    letter-spacing: 0.3px;
    color: var(--brand-blue);
  }
</style>
</head>
<body>
  <section class="card card--front">
    <div class="front-disc"></div>
    <div class="tagline-rule"></div>
    <p class="tagline">Assessments made simple</p>
  </section>

  <section class="card card--back">
    <div class="brand-disc"></div>
    <div class="brand-name">Velnor</div>

    <div class="person">
      <p class="person-name">Maarten Keizer</p>
      <p class="person-role">MANAGER</p>
    </div>

    <ul class="contact">
      <li><span class="contact-key">M</span>0150 7312846</li>
      <li><span class="contact-key">T</span>0655 274 1938</li>
      <li><span class="contact-key">E</span>keizer@velnor.nl</li>
    </ul>

    <address class="address">
      Lindenhoflaan 14<br>
      2514 BK&nbsp;&nbsp;'S-Gravenhage<br>
      NETHERLANDS
    </address>

    <p class="website">www.velnor.nl</p>
  </section>
</body>
</html>
```